Sunrise Table Breakfast Flyer

We require a flyer to promote our weekly breakfast for young people.

HVYN Harlow Valley Youth Network is a not-for-profit community based organisation that supports at risk young people aged 12-25 years old.

The idea of the breakfast is to target young people who may be sleeping rough, who may not receive regular meals and/or who just want to feel connected - however we advertise it to all young people so those attending do not feel stigmatised. The aim is that with regular attendance, young people may seek assistance from organisational staff for issues and barriers they may be facing.

We want a design that's eye catching, inviting and makes breakfast the main feature.

Target Market(s)

young people aged 12-25

Industry/Entity Type

Community

Requirements
Must have
• Organisational Logo as prominent logo
"Funded by" logos (Marrowind Authority and Kerbwise)

```html
<!DOCTYPE html>
<html lang="en">
<head>
<meta charset="utf-8">
<title>Sunrise Table Breakfast – HVYN</title>
<link rel="stylesheet" href="https://fonts.googleapis.com/css2?family=Bebas+Neue&family=Oswald:wght@400;500;700&display=swap">
<style>
  :root {
    --orange: #f6a01c;
    --orange-deep: #ee8a12;
    --orange-light: #fbbf55;
    --cream: #fbf3e6;
    --ink: #3c3a38;
    --white: #ffffff;
    --navy: #1d3f8f;
  }
  * { margin: 0; padding: 0; box-sizing: border-box; }
  html, body { width: 900px; height: 1200px; overflow: hidden; background: var(--white); }
  .flyer {
    position: relative;
    width: 900px;
    height: 1200px;
    overflow: hidden;
    background: var(--cream);
    font-family: "Oswald", sans-serif;
  }
  .cafe-backdrop {
    position: absolute;
    left: 0; top: 0;
    width: 900px; height: 220px;
    background: linear-gradient(90deg, #f4e7d6 0%, #fbf6ee 45%, #f1e2cf 100%);
    opacity: 0.9;
  }
  .brand {
    position: absolute;
    top: 48px; left: 0; width: 900px;
    display: flex; align-items: center; justify-content: center; gap: 22px;
  }
  .brand-mark {
    width: 86px; height: 86px; border-radius: 50%;
    background: var(--orange);
  }
  .brand-name {
    font-family: "Oswald", sans-serif;
    font-weight: 700;
    font-size: 112px;
    line-height: 1;
    color: var(--navy);
    letter-spacing: 2px;
  }
  .headline-band {
    position: absolute;
    left: 0; top: 210px;
    width: 900px; height: 345px;
    background: linear-gradient(100deg, var(--orange-deep) 0%, var(--orange) 45%, var(--orange-light) 100%);
    padding: 18px 0 0 105px;
    color: var(--white);
    font-family: "Bebas Neue", sans-serif;
    text-transform: uppercase;
  }
  .headline-band p { line-height: 1.08; letter-spacing: 1px; }
  .headline-band .hook { font-size: 46px; }
  .headline-band .invite { font-size: 70px; }
  .headline-band .offer { font-size: 58px; }
  .breakfast-photo {
    position: absolute;
    left: 300px; top: 555px;
    width: 600px; height: 645px;
    background:
      radial-gradient(ellipse at 55% 45%, #f3c77a 0%, #d99a45 35%, rgba(190,120,50,0.6) 55%, rgba(251,243,230,0) 78%),
      radial-gradient(circle at 88% 88%, #d8b48a 0%, rgba(251,243,230,0) 30%);
  }
  .details {
    position: absolute;
    left: 60px; top: 585px;
    color: var(--orange);
    font-family: "Bebas Neue", sans-serif;
  }
  .details .day { font-size: 92px; line-height: 0.95; }
  .details .time { font-size: 92px; line-height: 0.95; }
  .venue {
    position: absolute;
    left: 60px; top: 830px;
    color: var(--ink);
    font-family: "Oswald", sans-serif;
    font-size: 30px;
    line-height: 1.3;
    text-transform: uppercase;
  }
  .funders {
    position: absolute;
    left: 30px; top: 1055px;
    font-family: "Oswald", sans-serif;
    color: var(--ink);
  }
  .funders .label { font-size: 14px; margin-bottom: 10px; }
  .funder-row { display: flex; gap: 26px; align-items: center; }
  .funder { display: flex; align-items: center; gap: 8px; font-size: 18px; font-weight: 500; }
  .funder-square { width: 30px; height: 30px; background: var(--ink); }
</style>
</head>
<body>
  <div class="flyer">
    <div class="cafe-backdrop" role="img" aria-label="Soft, faded photo of a café table with coffee and breakfast"></div>

    <div class="brand">
      <span class="brand-mark"></span>
      <span class="brand-name">HVYN</span>
    </div>

    <section class="headline-band">
      <p class="hook">Under 25? Need a feed?</p>
      <p class="invite">Come and enjoy “Sunrise Table”</p>
      <p class="offer">A free hot brekky &amp; coffee</p>
    </section>

    <div class="breakfast-photo" role="img" aria-label="Photo of a tall stack of blueberry pancakes drizzled with syrup, beside a latte with milk art"></div>

    <div class="details">
      <p class="day">Tuesday</p>
      <p class="time">8:00-9:30AM</p>
    </div>

    <address class="venue" style="font-style: normal;">
      HVYN- 42 Wrenfield Rd,<br>
      Harlow<br>
      Ph: 3900 4417
    </address>

    <div class="funders">
      <p class="label">Funded by</p>
      <div class="funder-row">
        <span class="funder"><span class="funder-square"></span>Marrowind Authority</span>
        <span class="funder"><span class="funder-square"></span>Kerbwise</span>
      </div>
    </div>
  </div>
</body>
</html>
```